we can communicate on this, but i want to follow the approach we took on Pell|Quorn & Tillet but i feel the card front needs the black background and the platinum and gold logo. The back? I am open. we can use the same info from PQ&T. Vellum Crest is an enhanced equity investment fund - basically a very exclusive boutique hedge fund that uses only stock options. very advanced things. hope you are interested

Contact Information for Business Card

Dr. Owen T. Brisket, CFA
Scientifique de fusée financière
555.014.2296
TheDoc4793@mailvessel.example

4718 Fennel Brook Way N.
West Fargo, ND 58078

No web site

Colors

Designer to choose colors to be used in the design.

Requirements
Nice to have
• I tend to prefer the most visible applications of the logo to include logo and name, the logo version with a black background and the gold and platinum components separated by the black. I see this working well for a single side (logo and name - this is card front to me).
• I am fairly open to other treatments on the reverse side with the data. To me, it makes sense to have a different color rendition of the logo on the reverse and it may be a muted black tone on tone or an oversized portion that would have spot UV. Or, the reverse may play with colors and layout
Should not have
• Other colors = no no
• Decorative font

```html
<!DOCTYPE html>
<html lang="en">
<head>
<meta charset="utf-8">
<title>Vellum Crest — Business Card</title>
<link rel="stylesheet" href="https://fonts.googleapis.com/css2?family=Montserrat:wght@400;500;600;700&display=swap">
<style>
  :root {
    --stage: #2b2e33;
    --card-black: #0b0b0c;
    --band-top: #1a1a1b;
    --band-light: #2e2e30;
    --band-dark: #141415;
    --gold: #d9a923;
    --gold-light: #f3cf56;
    --gold-deep: #a97a10;
    --platinum: #c9c9cc;
    --white: #ffffff;
    --muted: #d4d4d6;
  }
  * { box-sizing: border-box; margin: 0; padding: 0; }
  html, body {
    width: 1200px; height: 801px; overflow: hidden;
    background: var(--stage);
    font-family: "Montserrat", sans-serif;
  }
  .canvas { position: relative; width: 1200px; height: 801px; }
  .card {
    position: absolute; top: 252px;
    width: 520px; height: 297px;
    background: var(--card-black);
    border-radius: 10px;
    overflow: hidden;
    box-shadow: 0 14px 30px rgba(0,0,0,.45);
  }
  .card--back { left: 50px; }
  .card--front { left: 630px; }
  .card-art { position: absolute; inset: 0; }

  /* back side */
  .person {
    position: absolute; left: 350px; top: 112px; color: var(--white);
  }
  .person-name {
    font-size: 17px; letter-spacing: .4px; text-transform: uppercase;
    font-weight: 400; white-space: nowrap;
  }
  .person-name strong { font-weight: 700; }
  .person-role {
    display: inline-block;
    margin-top: 5px; font-size: 8.5px; font-weight: 500; color: var(--muted);
    padding-bottom: 5px; border-bottom: 1.5px solid var(--platinum);
    position: relative; white-space: nowrap;
  }
  .person-role::after {
    content: ""; position: absolute; left: 0; bottom: -1.5px;
    width: 22px; height: 3px; background: var(--gold);
  }
  .contact-list {
    position: absolute; left: 28px; top: 150px; list-style: none;
    color: var(--white); font-size: 10.5px; font-weight: 500;
  }
  .contact-item {
    display: flex; align-items: center; gap: 12px; height: 21px;
    white-space: nowrap;
  }
  .contact-item--plain { padding-left: 23px; }
  .contact-icon { width: 11px; height: 11px; flex: none; fill: var(--muted); }

  /* front side */
  .frame {
    position: absolute; inset: 14px;
    border: 1.5px solid var(--gold);
  }
  .brand {
    position: absolute; left: 0; right: 0; top: 104px;
    display: flex; flex-direction: column; align-items: center; gap: 12px;
  }
  .brand-dot {
    width: 46px; height: 46px; border-radius: 50%;
    background: var(--gold);
  }
  .brand-name {
    font-size: 24px; font-weight: 700; letter-spacing: 1.5px;
    color: var(--white); text-transform: uppercase;
  }
</style>
</head>
<body>
<main class="canvas">

  <section class="card card--back" aria-label="Card back with contact details">
    <svg class="card-art" viewBox="0 0 520 297" aria-hidden="true">
      <defs>
        <linearGradient id="band" x1="0" y1="0" x2="1" y2="0">
          <stop offset="0" stop-color="#2e2e30"/>
          <stop offset="1" stop-color="#141415"/>
        </linearGradient>
        <linearGradient id="goldSheen" x1="0" y1="0" x2="1" y2="1">
          <stop offset="0" stop-color="#a97a10"/>
          <stop offset=".5" stop-color="#f3cf56"/>
          <stop offset="1" stop-color="#a97a10"/>
        </linearGradient>
      </defs>
      <rect x="0" y="0" width="520" height="297" fill="#0b0b0c"/>
      <path class="band" d="M0 90 H318 L298 250 H0 Z" fill="url(#band)"/>
      <path class="band-top" d="M0 0 H520 V90 H0 Z" fill="#1a1a1b"/>
      <path class="gold-slash" d="M326 40 L338 40 L310 262 L298 262 Z" fill="url(#goldSheen)"/>
      <path class="gold-corner" d="M0 92 Q4 20 62 6 Q22 36 10 100 Z" fill="url(#goldSheen)"/>
      <path class="gold-corner" d="M520 206 Q516 278 458 292 Q498 262 510 198 Z" fill="url(#goldSheen)"/>
    </svg>

    <div class="person">
      <p class="person-name"><strong>Owen</strong> Brisket</p>
      <p class="person-role">Scientifique de fusée financière</p>
    </div>

    <ul class="contact-list">
      <li class="contact-item">
        <svg class="contact-icon" viewBox="0 0 12 12"><path d="M6 0a4 4 0 0 0-4 4c0 3 4 8 4 8s4-5 4-8a4 4 0 0 0-4-4zm0 5.6A1.6 1.6 0 1 1 6 2.4a1.6 1.6 0 0 1 0 3.2z"/></svg>
        4718 Fennel Brook Way N.
      </li>
      <li class="contact-item contact-item--plain">West Fargo, ND 58078</li>
      <li class="contact-item">
        <svg class="contact-icon" viewBox="0 0 12 12"><path d="M2.4 0.5l2 2.2-1 1.5a7 7 0 0 0 4.4 4.4l1.5-1 2.2 2-1.3 1.9C5.6 11.2 .8 6.4.5 1.8z"/></svg>
        555.014.2296
      </li>
      <li class="contact-item">
        <svg class="contact-icon" viewBox="0 0 12 12"><path d="M0 2h12v8H0zm1 1v.4l5 3.2 5-3.2V3z"/></svg>
        TheDoc4793@mailvessel.example
      </li>
    </ul>
  </section>

  <section class="card card--front" aria-label="Card front with brand name">
    <div class="frame"></div>
    <div class="brand">
      <span class="brand-dot"></span>
      <p class="brand-name">Vellum Crest</p>
    </div>
  </section>

</main>
</body>
</html>
```